Telmoro Business Card

I already have the conplay logo. I need to develop a professional business card layout

Target Market(s)

Business

Industry/Entity Type

Business

Contact Information for Business Card

Company Name: Telmoro Limited

Font styles to use
Sans Serif

Colors

Designer to choose colors to be used in the design.

Requirements
Must have
• Use current logo
• Need two card size options:
• Small Card: 70mm x 28mm (Landscape)
• Square Card: 65mm x 65mm
Nice to have
• I will need 8-10 files for each name, number and email address (details to follow)

```html
<!DOCTYPE html>
<html lang="en">
<head>
<meta charset="utf-8">
<title>Telmoro Limited – Business Cards</title>
<link href="https://fonts.googleapis.com/css2?family=Roboto:wght@400;700;900&display=swap" rel="stylesheet">
<style>
  :root {
    --stage-dark: #050505;
    --stage-mid: #1c1d1f;
    --card-white: #ffffff;
    --ink: #222222;
    --ink-soft: #444444;
    --brand: #1f3a8a;
    --accent-gold: #e8a13a;
    --tone-green: #b9dd7a;
    --tone-blue: #8fcdf0;
    --tone-orange: #f6bd86;
    --tone-purple: #a9a1d6;
    --tone-red: #f2999e;
  }
  * { margin: 0; padding: 0; box-sizing: border-box; }
  html, body { width: 1200px; height: 880px; overflow: hidden; }
  body {
    position: relative;
    background: radial-gradient(ellipse at 50% 50%, var(--stage-mid) 0%, var(--stage-dark) 75%);
    font-family: "Roboto", Arial, sans-serif;
    color: var(--ink);
  }
  .card {
    position: absolute;
    background: var(--card-white);
    overflow: hidden;
    box-shadow: 0 0 0 1px #3a3a3a;
  }
  .card--small { left: 210px; top: 358px; width: 371px; height: 148px; }
  .card--square { left: 684px; top: 249px; width: 345px; height: 345px; }
  .card__art { position: absolute; left: 0; top: 0; }
  .brand { position: absolute; white-space: nowrap; line-height: 1; }
  .brand__name { font-weight: 900; color: var(--brand); letter-spacing: 0.5px; }
  .brand__suffix { font-weight: 400; color: var(--ink-soft); }
  .card--small .brand { left: 21px; top: 17px; }
  .card--small .brand__name { font-size: 29px; }
  .card--small .brand__suffix { font-size: 11px; margin-left: 2px; }
  .card--square .brand { left: 26px; top: 28px; }
  .card--square .brand__name { font-size: 35px; }
  .card--square .brand__suffix { font-size: 13px; margin-left: 2px; }
  .person { position: absolute; }
  .person__name { line-height: 1.1; color: var(--ink); }
  .person__role { line-height: 1.1; color: var(--ink); }
  .person__rule { border: 0; border-top: 1px solid var(--accent-gold); }
  .contact { list-style: none; }
  .contact__item { display: flex; align-items: center; line-height: 1.15; }
  .contact__icon { flex: none; }
  .card--small .person { left: 20px; top: 88px; }
  .card--small .person__name { font-size: 10px; }
  .card--small .person__role { font-size: 7px; letter-spacing: 0.3px; }
  .card--small .person__rule { width: 81px; margin: 3px 0 2px; }
  .card--small .contact { margin-left: -10px; }
  .card--small .contact__item { font-size: 9.5px; }
  .card--small .contact__icon { width: 8px; height: 8px; margin-right: 2px; }
  .card--square .person { left: 30px; top: 71px; }
  .card--square .person__name { font-size: 13px; }
  .card--square .person__role { font-size: 10px; letter-spacing: 0.3px; }
  .card--square .person__rule { width: 104px; margin: 3px 0 2px; }
  .card--square .contact { margin-left: -12px; }
  .card--square .contact__item { font-size: 13px; }
  .card--square .contact__icon { width: 10px; height: 10px; margin-right: 2px; }
</style>
</head>
<body>

<svg width="0" height="0" style="position:absolute">
  <defs>
    <linearGradient id="art-tones" x1="0" y1="1" x2="1" y2="0">
      <stop offset="0" stop-color="#8fcdf0"/>
      <stop offset="0.3" stop-color="#b9dd7a"/>
      <stop offset="0.55" stop-color="#f6bd86"/>
      <stop offset="0.8" stop-color="#a9a1d6"/>
      <stop offset="1" stop-color="#f2999e"/>
    </linearGradient>
    <symbol id="icon-mail" viewBox="0 0 10 10">
      <rect x="1" y="2.5" width="8" height="5.5" fill="none" stroke="#e8a13a" stroke-width="0.9"/>
      <path d="M1 2.5 L5 5.6 L9 2.5" fill="none" stroke="#e8a13a" stroke-width="0.9"/>
    </symbol>
    <symbol id="icon-phone" viewBox="0 0 10 10">
      <path d="M2.3 1.5 L3.8 1.5 L4.4 3.4 L3.4 4.1 Q4.3 5.8 5.9 6.6 L6.6 5.6 L8.5 6.2 L8.5 7.7 Q5.8 8.6 3.6 6.4 Q1.4 4.2 2.3 1.5 Z" fill="#e8a13a"/>
    </symbol>
  </defs>
</svg>

<!-- Small landscape card -->
<section class="card card--small">
  <svg class="card__art" width="371" height="148" viewBox="0 0 371 148" role="img" aria-label="Decorative diagonal band of multicolour stripes">
    <polygon points="236,148 332,0 371,0 371,148" fill="url(#art-tones)"/>
  </svg>
  <div class="brand">
    <span class="brand__name">TELMORO</span><span class="brand__suffix">Limited</span>
  </div>
  <div class="person">
    <p class="person__name">Ravi Mehta</p>
    <p class="person__role">Fashion Designer</p>
    <hr class="person__rule">
    <ul class="contact">
      <li class="contact__item"><svg class="contact__icon"><use href="#icon-mail"/></svg>hi@ravimehta.com</li>
      <li class="contact__item"><svg class="contact__icon"><use href="#icon-phone"/></svg>301 555 0274</li>
    </ul>
  </div>
</section>

<!-- Square card -->
<section class="card card--square">
  <svg class="card__art" width="345" height="345" viewBox="0 0 345 345" role="img" aria-label="Decorative diagonal band of multicolour stripes">
    <polygon points="150,345 330,74 345,74 345,345" fill="url(#art-tones)"/>
  </svg>
  <div class="brand">
    <span class="brand__name">TELMORO</span><span class="brand__suffix">Limited</span>
  </div>
  <div class="person">
    <p class="person__name">Ravi Mehta</p>
    <p class="person__role">Fashion Designer</p>
    <hr class="person__rule">
    <ul class="contact">
      <li class="contact__item"><svg class="contact__icon"><use href="#icon-mail"/></svg>hi@ravimehta.com</li>
      <li class="contact__item"><svg class="contact__icon"><use href="#icon-phone"/></svg>301 555 0274</li>
    </ul>
  </div>
</section>

</body>
</html>
```